Brisco & Thorne Price List for Dealers

Looking for a 4 pages total including front and back of catalog. Looking for a PDF that we can upload to a printer for production. Full color, professional looking. We have uploaded our current price list, just need to have it look a little more updated. See our website BriscoandThorne.com for more info on us, see our competitor QuillanandRusk.com, see our vendors Tovarin.com, Lumbrel.com, Zenquor.com, Pilv.com

Target Market(s)

automotive dealers, selling aftermarket products. Sunroofs, leather interiors, seat heaters, convertible top repairs, interior work see BriscoandThorne.com for info, also see our competitors quillanandrusk.com . See our vendors Tovarin.com, Lumbrel.com, Zenquor.com, Pilv.com

Industry/Entity Type

Automotive

Font styles to use
Serif

Colors

Designer to choose colors to be used in the design.

Requirements
Must have
• Logo, phone number, fax number, web address and email address which is INFO@BRISCOANDTHORNE.COM
Nice to have
• just looking for a nice, professional price list/catalog to hand out at auto dealers who sell our product.

```html
<!DOCTYPE html>
<html lang="en">
<head>
<meta charset="utf-8">
<title>Brisco &amp; Thorne Dealer Price List – Rear Sensing &amp; Mobile Video</title>
<link href="https://fonts.googleapis.com/css2?family=Tinos:wght@700&family=Zilla+Slab:wght@400&display=swap" rel="stylesheet">
<style>
  :root {
    --navy: #253a8a;
    --ink: #1f1f1f;
    --rule: #2a2a2a;
    --row-deep: #b4b1d4;
    --row-light: #d9d9e6;
    --row-plain: #ffffff;
    --paper: #ffffff;
  }
  html, body {
    margin: 0;
    padding: 0;
    width: 776px;
    height: 1200px;
    overflow: hidden;
    background: var(--paper);
  }
  .page {
    position: relative;
    width: 776px;
    height: 1200px;
    color: var(--ink);
    font-family: "Zilla Slab", Georgia, serif;
  }
  .price-table {
    position: absolute;
    left: 70px;
    width: 627px;
    border-collapse: collapse;
    table-layout: fixed;
    font-size: 21px;
    line-height: 1.2;
  }
  .price-table td {
    border: 2px solid var(--rule);
    text-align: center;
    vertical-align: middle;
    padding: 2px 12px;
  }
  .price-table .col-item { width: 314px; }
  .section-head td {
    background: var(--navy);
    color: #fff;
    font-family: "Tinos", "Times New Roman", serif;
    font-weight: 700;
    font-size: 22px;
    height: 36px;
    padding: 0;
  }
  .row-deep td { background: var(--row-deep); }
  .row-light td { background: var(--row-light); }
  .cell-plain { background: var(--row-plain) !important; }
  .cell-justify { text-align: justify !important; text-align-last: center; }
  .cell-top { vertical-align: top !important; padding-top: 4px !important; }

  .rear-sensing { top: 72px; }
  .mobile-video { top: 823px; }

  .section-title {
    position: absolute;
    top: 662px;
    left: 0;
    width: 776px;
    margin: 0;
    text-align: center;
    font-family: "Tinos", "Times New Roman", serif;
    font-weight: 700;
    font-size: 47px;
    color: var(--navy);
    letter-spacing: 0.5px;
  }
  .section-note {
    position: absolute;
    top: 726px;
    left: 120px;
    width: 536px;
    margin: 0;
    text-align: center;
    font-size: 21px;
    line-height: 27px;
  }
</style>
</head>
<body>
<main class="page">

  <table class="price-table rear-sensing">
    <colgroup><col class="col-item"><col></colgroup>
    <tr class="section-head"><td colspan="2">Rear Sensing Systems</td></tr>
    <tr class="row-deep" style="height:41px"><td>Blind Spot Sensors</td><td>$695.00</td></tr>
    <tr class="section-head"><td colspan="2">Backup Sensors</td></tr>
    <tr class="row-light" style="height:41px"><td>2 Sensor Set</td><td>$350.00</td></tr>
    <tr class="row-light" style="height:41px"><td>3 Sensor Set</td><td>$500.00</td></tr>
    <tr class="row-deep" style="height:37px"><td>Rear Camera Video System</td><td>$795.00</td></tr>
    <tr class="row-light" style="height:64px"><td>Rear Camer Awith Navigation Installation</td><td class="cell-top">$395.00</td></tr>
    <tr class="row-deep" style="height:66px"><td>Rear Camera Into Auto Dimming Mirror</td><td class="cell-top">$795.00*</td></tr>
    <tr class="row-light" style="height:70px"><td colspan="2">Optional Temperature/Compass/RoadLink<br>Call For Pricing</td></tr>
    <tr class="section-head"><td colspan="2">Advanced Rear View Mirror</td></tr>
    <tr class="row-light" style="height:70px"><td class="cell-justify">Auto-Dimming, Compass, Outside Temperature</td><td class="cell-top">$695.00</td></tr>
  </table>

  <h2 class="section-title">MOBILE/VIDEO</h2>
  <p class="section-note">All Units Include Monitor, Wireless Remote &amp; 2 Wireless Headphones. Audio Comes Through Vehicle’s Stereo System.</p>

  <table class="price-table mobile-video">
    <colgroup><col class="col-item"><col></colgroup>
    <tr class="row-light" style="height:70px"><td class="cell-plain cell-justify">All-n-One Overhead Flip Down Monitor W/DVD</td><td class="cell-top">$795.00</td></tr>
    <tr class="section-head"><td colspan="2">Headrest DVD Systems</td></tr>
    <tr class="row-light" style="height:64px"><td>7” Headrest Monitors – Black, Grey or Tan Leather</td><td class="cell-top">$995 to $1195.00</td></tr>
    <tr class="row-deep" style="height:72px"><td>9” Headrest Monitors – Black, Grey or Tan Leather</td><td class="cell-top">$1195 to $1395.00</td></tr>
  </table>

</main>
</body>
</html>
```